Harvest Table Gala 2022- FB poster ads

Design for our Harvest Table Gala Event
Designs 3 designs for Face Book Banner, posts and social Media ads
Each can look the same just different subjects on each
1. Design We're Back!
The Harvest Table Gala Is Back!
Ventura County’s Premier Food, Wine and Brew Event
August 14th
Vendor and ticket info at https://brightmeadowfair.com/

2. Vendors be a part of the event
The Harvest Table Gala is Back!
August 14th 2020
Vendors sign up today at
Vendor info at https://brightmeadowfair.com/

3. Sponsor info
The Harvest Table Gala
August 14th 2022
Check out our great Sponsorship opportunities
Sponsor info at https://brightmeadowfair.com/

Target Market(s)

Foodies, wine and beer enthusists

Industry/Entity Type

Farm to fork, fresh in season and local

Colors
00AB8E
00BBA5
67D7C9
C6EFE9
E9F9F6

Requirements
Should not have
• no fast food looking photos

```html
<!DOCTYPE html>
<html lang="en">
<head>
<meta charset="utf-8">
<title>Harvest Table Gala – Sponsor Banner</title>
<link rel="stylesheet" href="https://fonts.googleapis.com/css2?family=Lobster&family=Courgette&display=swap">
<style>
  :root {
    --backdrop: #808080;
    --paper: #f4f4f3;
    --paper-shade: #e6e7e6;
    --brown: #6b4234;
    --orange: #ef7c3a;
    --teal: #00ab8e;
    --teal-deep: #1a8a74;
    --teal-light: #00bba5;
    --white: #ffffff;
    --link-yellow: #f5c400;
  }
  * { margin: 0; padding: 0; box-sizing: border-box; }
  html, body {
    width: 1200px; height: 944px; overflow: hidden;
    background: var(--backdrop);
  }
  .banner {
    position: absolute; left: 52px; top: 186px;
    width: 1096px; height: 573px; overflow: hidden;
    background: linear-gradient(180deg, var(--white) 0%, var(--paper) 55%, var(--paper-shade) 100%);
  }
  .banner-shapes { position: absolute; inset: 0; }
  .headline-block {
    position: absolute; left: 20px; top: 40px; width: 460px;
    text-align: center;
  }
  .headline {
    font-family: "Lobster", cursive;
    color: var(--brown);
    font-weight: 400;
    line-height: 1;
  }
  .headline .lead { display: block; font-size: 38px; margin-bottom: 2px; }
  .headline .event-name { display: block; font-size: 54px; }
  .headline .back { display: block; font-size: 62px; margin-top: 6px; }
  .tagline {
    font-family: "Courgette", cursive;
    color: var(--brown);
    font-size: 21px;
    margin-top: 30px;
  }
  .event-detail {
    font-family: "Courgette", cursive;
    color: var(--orange);
    font-size: 39px;
    line-height: 1.38;
  }
  .brand {
    position: absolute; left: 48px; top: 452px;
    display: flex; align-items: center; gap: 10px;
  }
  .brand-dot {
    width: 34px; height: 34px; border-radius: 50%;
    background: var(--orange);
    flex: none;
  }
  .brand-name {
    font-family: "Courgette", cursive;
    color: var(--white);
    font-size: 22px;
    white-space: nowrap;
  }
  .sponsor-call {
    position: absolute; left: 339px; top: 450px;
    font-family: "Courgette", cursive;
    color: var(--white);
    font-size: 34px;
    line-height: 1.3;
    white-space: nowrap;
  }
  .sponsor-call .site { color: var(--link-yellow); }
</style>
</head>
<body>
  <section class="banner">
    <svg class="banner-shapes" width="1096" height="573" viewBox="0 0 1096 573">
      <defs>
        <linearGradient id="footerBand" x1="0" y1="0" x2="1" y2="0">
          <stop offset="0" stop-color="var(--teal)"/>
          <stop offset="0.7" stop-color="var(--teal)"/>
          <stop offset="1" stop-color="var(--teal-deep)"/>
        </linearGradient>
        <linearGradient id="mainDish" x1="0" y1="0" x2="1" y2="1">
          <stop offset="0" stop-color="#d9d3c4"/>
          <stop offset="0.5" stop-color="#9a6a48"/>
          <stop offset="1" stop-color="#e4dcbc"/>
        </linearGradient>
        <linearGradient id="breadDish" x1="0" y1="0" x2="1" y2="1">
          <stop offset="0" stop-color="#b99777"/>
          <stop offset="1" stop-color="#5b4536"/>
        </linearGradient>
        <linearGradient id="beefDish" x1="0" y1="0" x2="1" y2="1">
          <stop offset="0" stop-color="#b8394a"/>
          <stop offset="1" stop-color="#e8e4e2"/>
        </linearGradient>
      </defs>

      <path role="img" aria-label="Photo of sliced glazed pork tenderloin with spinach risotto on a white plate"
            d="M500 0 C490 170 640 352 800 347 C930 342 1040 292 1096 200 L1096 0 Z"
            fill="url(#mainDish)" stroke="var(--teal)" stroke-width="6"/>

      <path d="M0 408 C300 440 700 420 1096 378 L1096 392 C700 432 300 452 0 420 Z" fill="var(--orange)"/>
      <path d="M0 415 C300 447 700 428 1096 388 L1096 573 L0 573 Z" fill="url(#footerBand)"/>

      <circle role="img" aria-label="Photo of toasted bread slices topped with pâté"
              cx="649" cy="279" r="115" fill="url(#breadDish)" stroke="var(--white)" stroke-width="6"/>
      <circle role="img" aria-label="Photo of rolled rare beef with spinach leaves"
              cx="901" cy="330" r="76" fill="url(#beefDish)" stroke="var(--white)" stroke-width="6"/>
    </svg>

    <div class="headline-block">
      <h1 class="headline">
        <span class="lead">The</span>
        <span class="event-name">Harvest Table Gala</span>
        <span class="back">Is Back!</span>
      </h1>
      <p class="tagline">Ventura County’s Premier Food,</p>
      <p class="event-detail">Wine and Brew Event<br>August 14th 2022</p>
    </div>

    <div class="brand">
      <span class="brand-dot"></span>
      <span class="brand-name">Bright Meadow Fair</span>
    </div>

    <p class="sponsor-call">
      Check out our great Sponsorship opportunities<br>
      Sponsor info at <span class="site">https://brightmeadowfair.com/</span>
    </p>
  </section>
</body>
</html>
```